Business cards for KORBEN Real Estate Properties LLC

We need a cool, original business card design for a company based in the Washington DC metropolitan area. We are a new energetic and passionate Real Estate Investing Company that invests in all types of real estate; commercial, residential, industrial etc.

Our company color is Red since it reflects action, energy and speed; it is assertive confident, energizing, exciting, powerful, passionate and determined. So we would like business card communicate those qualities to the audience.

Our audiences are investors that want to invest with us, real estate sellers, buyers, and tenants who lease from us.

Our logo is attached

```html
<!DOCTYPE html>
<html lang="en">
<head>
<meta charset="utf-8">
<title>KORBEN Real Estate Properties LLC — Business Cards</title>
<link href="https://fonts.googleapis.com/css2?family=Open+Sans:wght@400;600;700&display=swap" rel="stylesheet">
<style>
  :root {
    --backdrop: #4b4440;
    --card-black: #1c1c1c;
    --card-black-edge: #141414;
    --gloss-grey: #3a3a3a;
    --brand-red: #d9252a;
    --text-white: #ffffff;
    --text-soft: #e6e6e6;
    --divider: #7a2a2a;
  }
  * { margin: 0; padding: 0; box-sizing: border-box; }
  html, body {
    width: 1200px; height: 799px; overflow: hidden;
    background: var(--backdrop);
    font-family: "Open Sans", Arial, sans-serif;
  }
  .canvas {
    position: relative; width: 1200px; height: 799px;
    display: flex; align-items: center; justify-content: center; gap: 60px;
  }
  .card {
    position: relative; width: 525px; height: 300px;
    background: var(--card-black);
    border-radius: 4px;
    box-shadow: 0 14px 30px rgba(0,0,0,.45);
    overflow: hidden;
  }
  /* back of card: tone-on-tone wordmark */
  .card--back { display: flex; align-items: center; justify-content: center; }
  .wordmark { display: flex; align-items: center; gap: 16px; color: var(--gloss-grey); }
  .wordmark__dot { width: 40px; height: 40px; border-radius: 50%; background: var(--gloss-grey); flex: none; }
  .wordmark__name { font-weight: 700; font-size: 54px; line-height: 1; letter-spacing: 1px; }
  .wordmark__sub { font-weight: 700; font-size: 13.5px; letter-spacing: .4px; margin-top: 6px; text-transform: uppercase; }

  /* front of card */
  .card--front { display: flex; }
  .card--front .brand {
    width: 290px; display: flex; align-items: center; justify-content: center;
  }
  .card--front .wordmark { color: var(--text-white); gap: 12px; }
  .card--front .wordmark__dot { background: var(--brand-red); width: 34px; height: 34px; }
  .card--front .wordmark__name { font-size: 44px; }
  .card--front .wordmark__sub { font-size: 11px; }
  .divider {
    position: absolute; left: 300px; top: 60px; width: 1px; height: 110px;
    background: linear-gradient(var(--card-black), var(--divider), var(--card-black));
  }
  .details { padding: 58px 0 0 28px; color: var(--text-soft); font-size: 13.5px; line-height: 1.35; }
  .details__name { color: var(--brand-red); font-weight: 700; font-size: 19px; line-height: 1.1; }
  .details__role { color: var(--text-white); font-size: 13px; margin-bottom: 14px; }
  .details__address { margin-bottom: 22px; }
  .contact { list-style: none; }
  .contact li { display: flex; align-items: center; gap: 8px; margin-bottom: 3px; }
  .contact svg { width: 11px; height: 11px; flex: none; fill: var(--brand-red); }
</style>
</head>
<body>
<main class="canvas">
  <section class="card card--back" aria-label="Card back">
    <div class="wordmark">
      <span class="wordmark__dot"></span>
      <div>
        <div class="wordmark__name">KORBEN</div>
        <div class="wordmark__sub">Real Estate Properties LLC</div>
      </div>
    </div>
  </section>

  <section class="card card--front" aria-label="Card front">
    <div class="brand">
      <div class="wordmark">
        <span class="wordmark__dot"></span>
        <div>
          <div class="wordmark__name">KORBEN</div>
          <div class="wordmark__sub">Real Estate Properties LLC</div>
        </div>
      </div>
    </div>
    <span class="divider"></span>
    <div class="details">
      <p class="details__name">Marcus Delgado</p>
      <p class="details__role">Partner</p>
      <p class="details__address">1480 K St NW<br>Suite 200-318<br>Washington DC 20006</p>
      <ul class="contact">
        <li>
          <svg viewBox="0 0 12 12" aria-hidden="true"><path d="M3 0h6a1 1 0 0 1 1 1v10a1 1 0 0 1-1 1H3a1 1 0 0 1-1-1V1a1 1 0 0 1 1-1zm.5 1.5v8h5v-8z"/></svg>
          <span>202.555.0147</span>
        </li>
        <li>
          <svg viewBox="0 0 12 12" aria-hidden="true"><path d="M0 2h12v8H0zm1 1v.4l5 3.3 5-3.3V3zm0 1.6V9h10V4.6L6 7.9z"/></svg>
          <span>mdelgado@korbenrep.com</span>
        </li>
        <li>
          <svg viewBox="0 0 12 12" aria-hidden="true"><path d="M6 0a6 6 0 1 0 0 12A6 6 0 0 0 6 0zm0 1c.7 0 1.5 1.5 1.7 4H4.3C4.5 2.5 5.3 1 6 1zM1 6.5h2.3c.1 1.8.5 3.3 1.1 4.2A5 5 0 0 1 1 6.5zM1 5.5a5 5 0 0 1 3.4-4.2C3.8 2.2 3.4 3.7 3.3 5.5zm3.3 1h3.4C7.5 9 6.7 11 6 11s-1.5-2-1.7-4.5zm4.4 0H11a5 5 0 0 1-3.4 4.2c.6-.9 1-2.4 1.1-4.2zm0-1c-.1-1.8-.5-3.3-1.1-4.2A5 5 0 0 1 11 5.5z"/></svg>
          <span>www.korbenrep.com</span>
        </li>
      </ul>
    </div>
  </section>
</main>
</body>
</html>
```